Profesional personal website needs design and business card

I need a business card with my professional name as a logo "Marlo Vitality" for my business. I am a Wellness Coach, consultant and trainer. So it should be professional, wellness oriented and modern.

Target Market(s)

Private clients, governments, corporations. Luxury and high market.

Industry/Entity Type

Health And Wellness

Contact Information for Business Card

Marlo Vitality should be the logo

Colors

Designer to choose colors to be used in the design.

Requirements
Must have
• Marlo Vitality
• Name: Tomás Arribal
• Wellness Coach, Consultant & Trainer.
• Website: www.marlovitality.example
• Phone:
• Spain (+34) 612 480 397
• (USA) +1 (555) 318 2046
Nice to have
• The most important is the design of "Marlo Vitality", as this is going to be my personal brand logo. It should be professional, wellness, high end and actual.
Should not have
• no golds, no baroque style..

```html
<!DOCTYPE html>
<html lang="en">
<head>
<meta charset="utf-8">
<title>Marlo Vitality – Business Card</title>
<link href="https://fonts.googleapis.com/css2?family=Roboto:wght@400;700&display=swap" rel="stylesheet">
<style>
  :root {
    --page-bg: #e9ebee;
    --card-bg: #ffffff;
    --brand-blue: #1f6fc8;
    --deep-blue: #0b4fa8;
    --sky-blue: #2aa0e0;
    --leaf-green: #3d9a1f;
    --ink-grey: #555b63;
    --white: #ffffff;
  }
  * { box-sizing: border-box; margin: 0; padding: 0; }
  html, body {
    width: 1200px; height: 800px; overflow: hidden;
    background: var(--page-bg);
    font-family: "Roboto", Arial, sans-serif;
  }
  .canvas { position: relative; width: 1200px; height: 800px; }
  .card {
    position: absolute; width: 560px; height: 320px;
    background: var(--card-bg);
    border-radius: 22px;
    overflow: hidden;
    box-shadow: 0 10px 30px rgba(20, 40, 70, 0.18);
  }
  .card--front { left: 320px; top: 50px; }
  .card--back  { left: 320px; top: 420px; }

  .brand { position: absolute; display: flex; align-items: center; gap: 12px; }
  .brand__dot { width: 30px; height: 30px; border-radius: 50%; background: var(--brand-blue); }
  .brand__name {
    font-weight: 400; font-size: 40px; color: var(--brand-blue);
    letter-spacing: 0.5px; white-space: nowrap;
  }
  .card--front .brand { left: 50%; top: 50%; transform: translate(-50%, -50%); }
  .card--back .brand { left: 34px; top: 112px; gap: 10px; }
  .card--back .brand__name { font-size: 30px; }
  .card--back .brand__dot { width: 24px; height: 24px; }

  .wave { position: absolute; inset: 0; width: 100%; height: 100%; }

  .person { position: absolute; right: 30px; top: 24px; text-align: right; }
  .person__name { font-weight: 700; font-size: 19px; color: var(--brand-blue); }
  .person__role { margin-top: 3px; font-size: 12.5px; color: var(--ink-grey); }

  .contact {
    position: absolute; right: 24px; bottom: 44px;
    list-style: none; color: var(--white); font-size: 12px;
  }
  .contact__item {
    display: flex; align-items: center; justify-content: flex-end;
    gap: 8px; line-height: 22px; white-space: nowrap;
  }
  .contact__icon { width: 16px; height: 16px; flex: none; }
</style>
</head>
<body>
<main class="canvas">

  <section class="card card--front" aria-label="Card front">
    <div class="brand">
      <span class="brand__dot" aria-hidden="true"></span>
      <span class="brand__name">Marlo Vitality</span>
    </div>
  </section>

  <section class="card card--back" aria-label="Card back">
    <svg class="wave" viewBox="0 0 560 320" aria-hidden="true">
      <path d="M560 78 C450 88 380 120 350 180 C320 250 250 300 140 320 L560 320 Z" fill="var(--deep-blue)"/>
      <path d="M560 78 C450 88 380 120 350 180 C340 200 330 215 318 230 C340 200 355 170 368 150 C400 105 470 85 560 82 Z" fill="var(--sky-blue)"/>
      <path d="M505 80 C430 100 372 130 346 180 C318 238 262 290 165 316 L152 316 C250 290 300 236 330 176 C358 122 420 96 505 80 Z" fill="var(--white)"/>
      <path d="M300 160 C292 225 245 275 100 298 L100 290 C232 266 282 220 300 160 Z" fill="var(--leaf-green)"/>
    </svg>

    <div class="brand">
      <span class="brand__dot" aria-hidden="true"></span>
      <span class="brand__name">Marlo Vitality</span>
    </div>

    <div class="person">
      <p class="person__name">Tomás Arribal</p>
      <p class="person__role">Coach, Consultant &amp; Trainer.</p>
    </div>

    <ul class="contact">
      <li class="contact__item">Spain (+34) 612 480 397
        <svg class="contact__icon" viewBox="0 0 16 16" aria-hidden="true"><circle cx="8" cy="8" r="7.5" fill="var(--white)"/><path d="M5.2 4.2l1.5-.4.8 2-1 .7c.4 1 1.1 1.8 2.1 2.3l.7-1 2 .8-.4 1.5c-3.2.2-6-2.6-5.7-5.9z" fill="var(--deep-blue)"/></svg>
      </li>
      <li class="contact__item">(USA) +1 (555) 318 2046
        <svg class="contact__icon" viewBox="0 0 16 16" aria-hidden="true"><circle cx="8" cy="8" r="7.5" fill="var(--white)"/><path d="M5.2 4.2l1.5-.4.8 2-1 .7c.4 1 1.1 1.8 2.1 2.3l.7-1 2 .8-.4 1.5c-3.2.2-6-2.6-5.7-5.9z" fill="var(--deep-blue)"/></svg>
      </li>
      <li class="contact__item">www.marlovitality.example
        <svg class="contact__icon" viewBox="0 0 16 16" aria-hidden="true"><circle cx="8" cy="8" r="7.5" fill="var(--white)"/><circle cx="8" cy="8" r="4.5" fill="none" stroke="var(--deep-blue)" stroke-width="1"/><ellipse cx="8" cy="8" rx="2" ry="4.5" fill="none" stroke="var(--deep-blue)" stroke-width="1"/><line x1="3.5" y1="8" x2="12.5" y2="8" stroke="var(--deep-blue)" stroke-width="1"/></svg>
      </li>
    </ul>
  </section>

</main>
</body>
</html>
```